Business Card for Coral Reef Shore Dive Lodge
Kelumpang Beach Resort & Dive Tour Sdn. Bhd.
Bright & Fun-filled
Harudin Bin Sulaiman Taib
QRT Marketing & HR Manager
C27-4, Meranti Square, Jalan Tuaran
88450 Kota Kinabalu, SABAH Malaysia.
kelumpangresort@mailnest.example
572918-K (KPL/LN 4721)
logo vector

```html
<!DOCTYPE html>
<html lang="en">
<head>
<meta charset="utf-8">
<title>Coral Reef Shore Dive Lodge – Business Card</title>
<link rel="stylesheet" href="https://fonts.googleapis.com/css2?family=Cormorant+Garamond:wght@500;600&display=swap">
<style>
  :root {
    --page: #e9e7e4;
    --card-black: #0d0b0a;
    --gold: #c59a72;
    --silver: #f1ede9;
    --ink: #2a1f18;
  }
  * { box-sizing: border-box; margin: 0; padding: 0; }
  html, body { width: 1200px; height: 980px; overflow: hidden; }
  body {
    background: var(--page);
    font-family: "Cormorant Garamond", Georgia, serif;
    position: relative;
  }
  .card {
    position: absolute;
    left: 250px;
    width: 700px;
    height: 400px;
    border-radius: 20px;
    background: var(--card-black);
    overflow: hidden;
    box-shadow: 0 6px 18px rgba(0,0,0,.18);
  }
  .card--back { top: 60px; }
  .card--front { top: 520px; }

  .brand {
    display: flex;
    align-items: center;
    gap: 14px;
    color: var(--gold);
    font-weight: 600;
    line-height: 1;
  }
  .brand__mark {
    flex: none;
    border-radius: 50%;
    background: var(--gold);
  }

  .card--back .brand {
    position: absolute;
    left: 0; right: 0; top: 170px;
    justify-content: center;
    font-size: 56px;
  }
  .card--back .brand__mark { width: 36px; height: 36px; }

  .wave { position: absolute; inset: 0; width: 100%; height: 100%; }

  .card--front .brand {
    position: absolute;
    left: 40px; top: 50px;
    font-size: 38px;
    gap: 10px;
  }
  .card--front .brand__mark { width: 24px; height: 24px; }

  .holder {
    position: absolute;
    left: 40px; top: 118px;
    color: var(--gold);
  }
  .holder__name { font-size: 21px; font-weight: 600; letter-spacing: .02em; }
  .holder__role { font-size: 15px; font-weight: 500; margin-top: 2px; }

  .contacts {
    position: absolute;
    left: 400px; top: 256px;
    width: 280px;
    list-style: none;
    color: var(--ink);
    font-size: 12px;
    font-weight: 600;
    line-height: 1.25;
  }
  .contacts li { display: flex; align-items: center; gap: 8px; margin-bottom: 3px; white-space: nowrap; }
  .contacts svg { width: 12px; height: 12px; flex: none; }
  .contacts .company { font-size: 11px; padding-left: 20px; margin-bottom: 1px; }
  .contacts .indent { padding-left: 20px; }
</style>
</head>
<body>

<section class="card card--back" aria-label="Card back">
  <div class="brand">
    <span class="brand__mark"></span>
    <span class="brand__name">Kelumpang</span>
  </div>
</section>

<section class="card card--front" aria-label="Card front">
  <svg class="wave" viewBox="0 0 700 400" preserveAspectRatio="none" aria-hidden="true">
    <defs>
      <linearGradient id="goldFill" x1="0" y1="0" x2="1" y2="1">
        <stop offset="0" stop-color="#b68a62"/>
        <stop offset=".45" stop-color="#d8b593"/>
        <stop offset="1" stop-color="#c79d76"/>
      </linearGradient>
    </defs>
    <path d="M0,188 C150,168 250,250 420,236 C540,226 620,214 700,230 L700,400 L0,400 Z" fill="#f1ede9"/>
    <path d="M0,200 C150,182 250,262 420,248 C540,238 620,226 700,242 L700,400 L0,400 Z" fill="url(#goldFill)"/>
  </svg>

  <div class="brand">
    <span class="brand__mark"></span>
    <span class="brand__name">Kelumpang</span>
  </div>

  <div class="holder">
    <div class="holder__name">Harudin Bin Sulaiman Taib</div>
    <div class="holder__role">QRT Marketing &amp; HR Manager</div>
  </div>

  <ul class="contacts">
    <li class="company">Kelumpang Beach Resort &amp; Dive Tour Sdn. Bhd.</li>
    <li class="company">572918-K (KPL/LN 4721)</li>
    <li>
      <svg viewBox="0 0 12 12"><circle cx="6" cy="6" r="6" fill="#2a1f18"/><path d="M6 2.6a2 2 0 0 0-2 2c0 1.5 2 4.2 2 4.2s2-2.7 2-4.2a2 2 0 0 0-2-2z" fill="#e3c3a3"/></svg>
      C27-4, Meranti Square, Jalan Tuaran,
    </li>
    <li class="indent">88450 Kota Kinabalu, SABAH Malaysia.</li>
    <li>
      <svg viewBox="0 0 12 12"><circle cx="6" cy="6" r="6" fill="#2a1f18"/><path d="M4 3l1.2 1.4-.6.8c.4.9 1.1 1.6 2 2l.8-.6L9 7.8 8.2 9C6 8.8 3.2 6 3 3.8z" fill="#e3c3a3"/></svg>
      Tel: +6088 274 510
    </li>
    <li>
      <svg viewBox="0 0 12 12"><circle cx="6" cy="6" r="6" fill="#2a1f18"/><rect x="3.2" y="4" width="5.6" height="4" fill="#e3c3a3"/></svg>
      Fax: +6088 274 511
    </li>
    <li>
      <svg viewBox="0 0 12 12"><circle cx="6" cy="6" r="6" fill="#2a1f18"/><rect x="4.3" y="2.6" width="3.4" height="6.8" rx=".6" fill="#e3c3a3"/></svg>
      H/P: +6013 882 4107
    </li>
    <li>
      <svg viewBox="0 0 12 12"><circle cx="6" cy="6" r="6" fill="#2a1f18"/><rect x="3" y="3.8" width="6" height="4.4" fill="#e3c3a3"/><path d="M3 3.8l3 2.4 3-2.4" stroke="#2a1f18" stroke-width=".7" fill="none"/></svg>
      kelumpangresort@mailnest.example
    </li>
  </ul>
</section>

</body>
</html>
```